Postcard Design

www.tovil.com.au
i am an occupational therapist and professionally trained coach. i work with children, parents and disability service providers to achieve brilliant outcomes for children with special needs.
http://www.tovil.com.au/service/for-families
I need a postcard to give parents to promote our family service coaching service
A family service coach will work with you to set specific goals for your child, build a dream team, design and manage your child's highly effective therapy and educational team to ensure brilliant outcomes for your child..
KORBU - you have done my business card previously. they were great thank you.

```html
<!DOCTYPE html>
<html lang="en">
<head>
<meta charset="utf-8">
<title>Tovil – Family Service Coaching Postcard</title>
<link rel="stylesheet" href="https://fonts.googleapis.com/css2?family=Montserrat:wght@400;600;700&family=Titan+One&family=Fredoka:wght@600&display=swap">
<style>
  :root {
    --brand-blue: #5b7db8;
    --brand-blue-deep: #2f4c86;
    --title-blue: #8aa8dc;
    --charcoal: #3a3a3d;
    --paper: #ffffff;
    --stage: #e6e7e9;
    --stamp: #ececec;
    --rule: #e2e2e2;
    --photo-hands-dark: #4f565f;
    --photo-hands-mid: #737b85;
    --photo-hands-warm: #a9897a;
    --photo-family-light: #cfc9bd;
    --photo-family-mid: #a7a8ab;
    --photo-family-blue: #5f7296;
  }
  * { box-sizing: border-box; margin: 0; padding: 0; }
  html, body { width: 1200px; height: 740px; overflow: hidden; }
  body {
    position: relative;
    background: var(--stage);
    font-family: "Montserrat", Arial, sans-serif;
    color: var(--paper);
  }

  .postcard { position: absolute; overflow: hidden; }

  /* ---------- Front ---------- */
  .postcard-front {
    left: 50px; top: 135px; width: 548px; height: 423px;
    background: var(--charcoal);
  }
  .front-header {
    position: absolute; left: 0; top: 0; width: 100%; height: 93px;
    background: var(--brand-blue);
  }
  .brand {
    position: absolute; display: flex; align-items: center; gap: 8px;
    font-family: "Montserrat", Arial, sans-serif; font-weight: 600;
    color: var(--paper);
  }
  .brand-dot { display: block; border-radius: 50%; background: var(--paper); }
  .front-header .brand { left: 38px; top: 28px; font-size: 27px; }
  .front-header .brand-dot { width: 30px; height: 30px; }
  .front-tagline {
    position: absolute; left: 258px; top: 27px; width: 285px;
    font-size: 12.6px; line-height: 15px;
  }
  .front-tagline strong { display: block; font-weight: 700; }
  .front-tagline span { display: block; font-size: 12.6px; margin-top: 1px; }

  .front-photo {
    position: absolute; left: 0; top: 93px; width: 100%; height: 230px;
    background:
      radial-gradient(ellipse 45% 55% at 48% 55%, var(--photo-hands-warm) 0%, transparent 100%),
      linear-gradient(100deg, var(--photo-hands-mid) 0%, var(--photo-hands-dark) 55%, var(--photo-hands-mid) 100%);
  }
  .front-title {
    position: absolute; left: 0; top: 105px; width: 100%;
    text-align: center;
    font-family: "Titan One", "Arial Black", sans-serif;
    font-weight: 400;
    font-size: 30px; letter-spacing: 0.2px;
    color: var(--title-blue);
    -webkit-text-stroke: 2px var(--paper);
    paint-order: stroke fill;
  }
  .front-swoosh { position: absolute; left: 0; top: 0; width: 548px; height: 423px; }
  .about-box {
    position: absolute; left: 108px; top: 308px; width: 332px; height: 64px;
    background: var(--brand-blue);
    padding: 5px 10px;
    text-align: center; font-size: 8px; line-height: 10px;
  }
  .about-box p + p { margin-top: 8px; }
  .about-box strong { font-weight: 700; }
  .front-web {
    position: absolute; left: 108px; top: 390px; width: 332px;
    display: flex; align-items: center; gap: 6px;
    font-size: 12.5px; letter-spacing: 2.4px; font-weight: 600;
  }
  .front-web::before, .front-web::after {
    content: ""; flex: 1; height: 2px; background: var(--paper);
  }

  /* ---------- Back ---------- */
  .postcard-back {
    left: 631px; top: 188px; width: 550px; height: 424px;
    background: var(--paper);
  }
  .back-panel { position: absolute; left: 0; top: 0; width: 266px; height: 352px; }
  .back-header {
    position: absolute; left: 0; top: 0; width: 100%; height: 72px;
    background: var(--brand-blue);
  }
  .back-header .brand { left: 64px; top: 20px; font-size: 25px; }
  .back-header .brand-dot { width: 28px; height: 28px; }
  .back-photo {
    position: absolute; left: 0; top: 72px; width: 100%; height: 218px;
    background: linear-gradient(160deg, var(--photo-family-light) 0%, var(--photo-family-mid) 50%, var(--photo-family-blue) 100%);
  }
  .service-list {
    position: absolute; left: 86px; top: 194px;
    list-style: none;
    font-family: "Fredoka", "Montserrat", sans-serif; font-weight: 600;
    font-size: 10.6px; line-height: 12.6px; letter-spacing: 0.1px;
    -webkit-text-stroke: 2px var(--brand-blue-deep);
    paint-order: stroke fill;
  }
  .service-list li { position: relative; padding-left: 10px; white-space: nowrap; }
  .service-list li::before {
    content: ""; position: absolute; left: 0; top: 3.5px;
    width: 6px; height: 6px; border-radius: 50%; background: var(--paper);
  }
  .back-band {
    position: absolute; left: 0; top: 290px; width: 100%; height: 62px;
    background: var(--charcoal);
  }
  .contact-box {
    position: absolute; left: 38px; top: 280px; width: 198px; height: 54px;
    background: linear-gradient(var(--title-blue), var(--brand-blue));
    border: 3px solid #cdd9ee; border-radius: 6px;
    padding: 3px 10px; font-size: 8.6px; line-height: 10.5px;
  }
  .contact-box h2 { font-size: 8.8px; font-weight: 700; }
  .contact-row { display: flex; }
  .contact-row dt { width: 48px; font-weight: 700; }
  .contact-row dd::before { content: ": "; }

  .stamp-box {
    position: absolute; left: 432px; top: 15px; width: 90px; height: 113px;
    background: var(--stamp); border: 1px solid #dcdcdc;
  }
  .address-lines { position: absolute; left: 289px; top: 268px; width: 236px; }
  .address-lines span { display: block; height: 2px; background: var(--rule); margin-bottom: 23px; }
</style>
</head>
<body>

<section class="postcard postcard-front" aria-label="Postcard front">
  <header class="front-header">
    <div class="brand"><span class="brand-dot"></span>tovil</div>
    <div class="front-tagline">
      <strong>Occupational Therapist Coach,<br>Speaker and Author</strong>
      <span>maren@tovil.com.au Mobile 0400 123 987</span>
    </div>
  </header>

  <div class="front-photo" role="img" aria-label="Photo of hands joining colourful jigsaw puzzle pieces"></div>
  <h1 class="front-title">DISABILITY SERVICE COACHING</h1>

  <svg class="front-swoosh" viewBox="0 0 548 423" aria-hidden="true">
    <path d="M0,258 Q250,330 548,272 L548,423 L0,423 Z" fill="#ffffff"/>
    <path d="M0,274 Q250,342 548,284 L548,423 L0,423 Z" fill="#5b7db8"/>
    <path d="M0,290 Q250,352 548,302 L548,423 L0,423 Z" fill="#3a3a3d"/>
  </svg>

  <div class="about-box">
    <p><strong>Maren Holt is</strong> an Occupational Therapist, Coach and Speaker who works with children, parents and disability service providers to achieve brilliant outcomes for children with special needs.</p>
    <p><strong>Tovil:</strong> [Toh-vil] the steady process of growing brilliant futures.</p>
  </div>

  <div class="front-web">WWW.TOVIL.COM.AU</div>
</section>

<section class="postcard postcard-back" aria-label="Postcard back">
  <div class="back-panel">
    <header class="back-header">
      <div class="brand"><span class="brand-dot"></span>tovil</div>
    </header>
    <div class="back-photo" role="img" aria-label="Photo of a smiling family with young children and a therapist"></div>
    <ul class="service-list">
      <li>Occupational Therapy</li>
      <li>Private Practice Coaching</li>
      <li>Family Service Coaching</li>
      <li>Clinical Supervision &amp; Workshops</li>
      <li>School Support</li>
      <li>Life Coaching</li>
    </ul>
    <div class="back-band"></div>
    <div class="contact-box">
      <h2>Contact Info</h2>
      <dl>
        <div class="contact-row"><dt>Phone</dt><dd>0400 123 987</dd></div>
        <div class="contact-row"><dt>Email</dt><dd>maren@tovil.com.au</dd></div>
        <div class="contact-row"><dt>Web</dt><dd>www.tovil.com.au</dd></div>
      </dl>
    </div>
  </div>

  <div class="stamp-box" aria-label="Stamp area"></div>
  <div class="address-lines" aria-label="Address lines">
    <span></span><span></span><span></span><span></span>
  </div>
</section>

</body>
</html>
```